Lantern Bridge - Tax season post card

We need postcard designed for a service firm, The Lantern Bridge LLC primarily for the tax season and also to promote our other service areas. We would like the use of our logo and prefer the orange, green, white color combinations but also open to suggestions. Use the three logos from the attached tax alert flyerThe Lantern Bridge is one stop shop for all your accounting, finance and compliance needs. The firm provides the following services-Accounting & BookkeepingBusiness Advisory Immigration Consulting Income tax preparationIRS RepresentationNon-profit AuditsNotary PublicPayroll and Sales taxLive-Scan fingerprintingProperty ManagementRetirement PlanningThe firm is managed by highly qualified and experienced CPA's, Enrolled Agents, and California Certified Tax Professionals. We give 25% discount for the first time client utilizing our accounting & book-keeping, audit services from your prior year CPA's fees.For the tax season we have $50 discount for our first time clientsTax preparation and consulting include, Trusts, Estates, S-Corp, C-Corp, Partnership, Non-Profit, and Individual Returns2605 Pacific AvenueStockton, CA 95204Phone: 209.463.4436Email: marla.lanternbridge@quillpost.example

Target Market(s)

Businesses and individuals looking for accountant

Industry/Entity Type

Accounting

Font styles to use
Serif

Colors
ec1f27
f37122
ffcf3e

Requirements
Must have
• All services listed
Nice to have
• Attractive logo and fonts
Should not have
• clutter. Too much content tightly adjusted

```html
<!DOCTYPE html>
<html lang="en">
<head>
<meta charset="utf-8">
<title>The Lantern Bridge LLC – Tax Season Postcard</title>
<link href="https://fonts.googleapis.com/css2?family=Oswald:wght@500;600;700&family=Lato:wght@400;700&display=swap" rel="stylesheet">
<style>
  :root{
    --red:#ec1f27;
    --orange:#f37122;
    --yellow:#ffcf3e;
    --green:#8cc63f;
    --ink:#1f1f1f;
    --band:#1c1c1c;
    --paper:#ffffff;
    --mist:#efefef;
    --stage:#e8e4de;
  }
  *{margin:0;padding:0;box-sizing:border-box}
  html,body{width:907px;height:1200px;overflow:hidden}
  body{background:var(--stage);position:relative;font-family:"Lato",Arial,sans-serif;color:var(--ink)}

  .card{position:absolute;width:723px;height:560px;background:linear-gradient(180deg,#fff 0%,var(--mist) 100%);overflow:hidden;box-shadow:0 2px 8px rgba(0,0,0,.25)}
  .card--front{left:95px;top:28px}
  .card--back{left:91px;top:610px;width:724px}
  .card svg.shapes{position:absolute;left:0;top:0}

  .brand{position:absolute;left:545px;top:128px;display:flex;align-items:center;gap:8px;font-size:13px;color:var(--ink)}
  .brand__dot{width:12px;height:12px;border-radius:50%;background:var(--orange)}
  .offer__amount{position:absolute;right:27px;top:194px;font-family:"Oswald",sans-serif;font-weight:600;font-size:35px;line-height:1;color:var(--red);letter-spacing:0}
  .offer__note{position:absolute;right:27px;top:240px;font-size:22px;color:var(--ink)}
  .alert{position:absolute;left:546px;top:298px;width:142px;height:30px;border-radius:15px 0 0 15px;background:var(--red);color:#fff;font-family:"Oswald",sans-serif;font-weight:500;font-size:16px;line-height:30px;text-align:center}

  .points{position:absolute;list-style:none;font-size:13.5px;line-height:18px;color:#222;text-align:justify;hyphens:manual}
  .points li{position:relative;padding-left:14px;margin-bottom:4px}
  .points li::before{content:"";position:absolute;left:0;top:6px;width:7px;height:7px;border-radius:50%;background:var(--red)}
  .points--left{left:44px;top:356px;width:298px}
  .points--right{left:394px;top:359px;width:290px}
  .points--right li{margin-bottom:10px}

  .cta{position:absolute;left:50px;top:508px;font-family:"Lato",sans-serif;font-weight:700;font-size:18px;color:#fff}
  .cta span{color:var(--orange)}
  .partner{position:absolute;background:#f4f4f4;border-radius:3px}
  .partner--one{left:447px;top:497px;width:92px;height:30px}
  .partner--two{left:585px;top:494px;width:88px;height:40px}

  .stamp{position:absolute;left:614px;top:23px;width:63px;height:67px;background:#c7c5c4}
  .address-line{position:absolute;left:454px;width:194px;height:1px;background:#bdbdbd}

  .list-title{position:absolute;font-family:"Oswald",sans-serif;font-weight:600;font-size:13.5px;color:var(--red);letter-spacing:.3px}
  .services{position:absolute;list-style:none;font-size:13.5px;line-height:17px;color:#222}
  .services li{position:relative;padding-left:10px;margin-bottom:6px}
  .services li::before{content:"";position:absolute;left:0;top:6px;width:6px;height:6px;border-radius:50%;background:var(--orange)}

  .contact{position:absolute;font-size:12.5px;line-height:16px;color:#eee}
  .icon{position:absolute}
</style>
</head>
<body>

<section class="card card--front">
  <svg class="shapes" width="723" height="560" viewBox="0 0 723 560">
    <defs>
      <linearGradient id="teamTone" x1="0" y1="0" x2="1" y2="1">
        <stop offset="0" stop-color="#9aa3ab"/>
        <stop offset=".5" stop-color="#5d5f63"/>
        <stop offset="1" stop-color="#c9a27a"/>
      </linearGradient>
    </defs>
    <path role="img" aria-label="Photo of a smiling team of tax professionals gathered around a meeting table with a laptop"
      d="M0,0 L510,0 C525,40 525,80 515,100 C490,190 450,255 390,285 C310,330 220,340 150,335 C90,330 40,320 0,305 Z"
      fill="url(#teamTone)"/>
    <g fill="none" stroke-linecap="butt">
      <path d="M510,-2 C525,40 525,75 518,92" stroke="var(--red)" stroke-width="24"/>
      <path d="M514,106 C490,190 450,255 395,282" stroke="var(--orange)" stroke-width="28"/>
      <path d="M383,290 C310,330 220,340 150,335" stroke="var(--yellow)" stroke-width="24"/>
      <path d="M140,334 C90,330 40,320 0,305" stroke="var(--green)" stroke-width="12"/>
    </g>
    <path d="M723,427 C600,450 480,470 340,480 L340,484 C480,475 600,455 723,431 Z" fill="var(--green)"/>
    <path d="M0,470 C100,478 220,485 360,480 L360,484 C220,490 100,484 0,477 Z" fill="var(--orange)"/>
    <path d="M0,484 C200,494 450,472 723,450 L723,560 L0,560 Z" fill="var(--band)"/>
  </svg>

  <div class="brand"><span class="brand__dot"></span>The Lantern Bridge, LLC</div>
  <div class="offer__amount">$50 DISCOUNT</div>
  <div class="offer__note">for our first time clients</div>
  <div class="alert">TAX SEASON ALERT</div>

  <ul class="points points--left">
    <li>Let the Lantern Bridge prepare your 2015 Corporate, Individual and all types of tax returns.</li>
    <li>The Lantern Bridge is managed by experi&shy;enced and highly qualified CPAs and Enrolled IRS agents</li>
  </ul>
  <ul class="points points--right">
    <li>All new, first time clients will receive a special $50 discount for this tax season</li>
    <li>Our office is conveniently located on the Miracle Mile, next to Brewhaven Coffee!</li>
  </ul>

  <div class="cta"><span>CALL TODAY</span> 209-555-0142</div>
  <div class="partner partner--one"></div>
  <div class="partner partner--two"></div>
</section>

<section class="card card--back">
  <svg class="shapes" width="724" height="560" viewBox="0 0 724 560">
    <defs>
      <linearGradient id="panelTone" x1="0" y1="0" x2="0" y2="1">
        <stop offset="0" stop-color="#ffffff"/>
        <stop offset="1" stop-color="#e6e6e6"/>
      </linearGradient>
      <linearGradient id="chartTone" x1="0" y1="0" x2="1" y2="0">
        <stop offset="0" stop-color="#6f757c"/>
        <stop offset=".6" stop-color="#b9c3cc"/>
        <stop offset="1" stop-color="#d9d4d2"/>
      </linearGradient>
    </defs>
    <rect width="724" height="560" fill="#fff"/>
    <path d="M297,0 C350,0 382,100 384,200 L387,560 L0,560 L0,0 Z" fill="var(--orange)"/>
    <path d="M289,0 C342,0 374,100 376,200 L378,560 L0,560 L0,0 Z" fill="var(--band)"/>
    <path d="M280,0 C333,0 364,100 366,200 L368,560 L0,560 L0,0 Z" fill="url(#panelTone)"/>
    <path role="img" aria-label="Photo of a businessman touching a glowing growth chart on a transparent screen"
      d="M0,0 L280,0 C320,0 344,60 352,190 L0,190 Z" fill="url(#chartTone)"/>
    <rect x="0" y="190" width="358" height="4" fill="var(--green)"/>
    <rect x="0" y="487" width="370" height="3" fill="var(--green)"/>
    <rect x="0" y="490" width="372" height="70" fill="var(--band)"/>
  </svg>

  <div class="stamp"></div>
  <div class="address-line" style="top:215px"></div>
  <div class="address-line" style="top:256px"></div>
  <div class="address-line" style="top:302px"></div>

  <div class="list-title" style="left:134px;top:205px">TAX OPTIONS</div>
  <ul class="services" style="left:22px;top:228px">
    <li>Tax Options</li>
    <li>Earned Income Credits</li>
    <li>Trusts &amp; Estates</li>
    <li>ITIN 990, 1120 &amp; 1040</li>
  </ul>
  <ul class="services" style="left:217px;top:232px">
    <li>Rapid refund</li>
    <li>IRS Representation</li>
    <li>Sales Tax and<br>Payroll Taxes</li>
  </ul>

  <div class="list-title" style="left:131px;top:334px">OTHER SERVICES</div>
  <ul class="services" style="left:25px;top:358px">
    <li>Business Advisory</li>
    <li>Immigration Consulting<br>Non-profit Audits</li>
    <li>Notary Public</li>
    <li>Live-Scan fingerprinting</li>
  </ul>
  <ul class="services" style="left:219px;top:358px">
    <li>Accounting &amp;<br>Bookkeeping</li>
    <li>Property<br>Management</li>
  </ul>

  <svg class="icon" style="left:26px;top:502px" width="9" height="12" viewBox="0 0 9 12">
    <path d="M4.5,0 C2,0 0,2 0,4.5 C0,7.5 4.5,12 4.5,12 C4.5,12 9,7.5 9,4.5 C9,2 7,0 4.5,0 Z M4.5,6 A1.6,1.6 0 1 1 4.5,2.8 A1.6,1.6 0 1 1 4.5,6 Z" fill="var(--orange)"/>
  </svg>
  <div class="contact" style="left:37px;top:501px">4817 Hollow Birch Lane<br>Stockton, CA 95871</div>
  <svg class="icon" style="left:184px;top:503px" width="11" height="11" viewBox="0 0 11 11">
    <circle cx="5.5" cy="5.5" r="5.5" fill="var(--orange)"/>
    <path d="M3.4,2.8 L4.4,2.6 L5,4 L4.4,4.6 C4.8,5.5 5.5,6.2 6.4,6.6 L7,6 L8.4,6.6 L8.2,7.6 C6,8 3,5 3.4,2.8 Z" fill="#1c1c1c"/>
  </svg>
  <div class="contact" style="left:199px;top:501px">209-555-0142</div>
  <svg class="icon" style="left:184px;top:520px" width="11" height="11" viewBox="0 0 11 11">
    <circle cx="5.5" cy="5.5" r="5.5" fill="var(--orange)"/>
  </svg>
  <div class="contact" style="left:199px;top:518px">www.lanternbridgellc.example</div>
</section>

</body>
</html>
```